Business Card

We are looking to re-create our business card. Attached is the company logo. we would like it to be back and front. for example one side with the persons information and the other side with the company logo. Be as creative as you would like but also keep in mind, we are a Health Insurance company and we need to look professional as well.
Business

```html
<!DOCTYPE html>
<html lang="en">
<head>
<meta charset="utf-8">
<title>Clearbrook Health Plans – Business Card</title>
<link rel="stylesheet" href="https://fonts.googleapis.com/css2?family=Source+Sans+3:wght@400;600;700&display=swap">
<style>
  :root {
    --page-bg: #e9ebed;
    --card-bg: #ffffff;
    --brand-blue: #1a93cf;
    --soft-blue: #9fcbea;
    --text-grey: #6e6e70;
    --rule-grey: #c9c9cb;
  }
  * { box-sizing: border-box; margin: 0; padding: 0; }
  html, body {
    width: 1200px; height: 873px; overflow: hidden;
    background: var(--page-bg);
    font-family: "Source Sans 3", "Myriad Pro", Arial, sans-serif;
  }
  .canvas {
    width: 1200px; height: 873px;
    display: flex; align-items: center; justify-content: center; gap: 60px;
  }
  .card {
    position: relative;
    width: 525px; height: 300px;
    background: var(--card-bg);
    box-shadow: 0 6px 18px rgba(0,0,0,0.12);
  }

  /* Contact side */
  .card-contact .decor-square {
    position: absolute; top: 28px; right: 40px;
    width: 110px; height: 110px;
    background: var(--soft-blue);
  }
  .holder {
    position: absolute; top: 158px; right: 40px; text-align: right;
  }
  .holder-name {
    font-size: 22px; font-weight: 700; color: var(--brand-blue); line-height: 1.1;
    white-space: nowrap;
  }
  .holder-title {
    font-size: 13px; font-weight: 600; color: var(--text-grey); margin-top: 3px;
    white-space: nowrap;
  }
  .contact-row {
    position: absolute; left: 26px; right: 26px; bottom: 30px;
    display: flex; align-items: center; justify-content: space-between;
  }
  .contact-item {
    display: flex; align-items: center; gap: 7px;
    font-size: 12px; color: var(--brand-blue); line-height: 1.3;
    white-space: nowrap; flex: none;
  }
  .contact-item svg { width: 15px; height: 15px; flex: none; fill: var(--brand-blue); }
  .contact-divider {
    width: 1px; height: 30px; background: var(--rule-grey); flex: none;
  }

  /* Brand side */
  .brand-lockup {
    position: absolute; top: 34px; left: 34px;
    display: flex; align-items: center; gap: 12px;
  }
  .brand-dot { width: 14px; height: 14px; background: var(--brand-blue); }
  .brand-name {
    font-size: 26px; font-weight: 400; color: var(--brand-blue); letter-spacing: 0.2px;
    white-space: nowrap;
  }
  .card-brand .decor-square {
    position: absolute; right: 44px; bottom: 40px;
    width: 130px; height: 130px;
    background: var(--brand-blue);
  }
</style>
</head>
<body>
<main class="canvas">

  <section class="card card-contact" aria-label="Card front: contact details">
    <div class="decor-square"></div>

    <div class="holder">
      <p class="holder-name">Dana R. Whitfield</p>
      <p class="holder-title">Health and Safety Specialist</p>
    </div>

    <div class="contact-row">
      <div class="contact-item">
        <svg viewBox="0 0 16 16" aria-hidden="true"><path d="M8 0a5.5 5.5 0 0 0-5.5 5.5C2.5 9.6 8 16 8 16s5.5-6.4 5.5-10.5A5.5 5.5 0 0 0 8 0zm0 7.6a2.1 2.1 0 1 1 0-4.2 2.1 2.1 0 0 1 0 4.2z"/></svg>
        <span>412 Orchard Lane<br>Marlow, CA 95012</span>
      </div>
      <div class="contact-divider"></div>
      <div class="contact-item">
        <svg viewBox="0 0 16 16" aria-hidden="true"><path d="M3.6 0.8l2.2 2.7c.3.4.3.9 0 1.3L4.7 6.1c.9 2 2.6 3.8 4.6 4.8l1.3-1.1c.4-.3.9-.3 1.3 0l2.7 2.2c.4.3.4.9.1 1.3l-1.3 1.5c-.5.5-1.2.7-1.9.5C6.2 14.1 1.9 9.8.7 4.4.5 3.7.7 3 1.2 2.5L2.3 1.3c.4-.4 1-.9 1.3-.5z"/></svg>
        <span>555-014-2386</span>
      </div>
      <div class="contact-divider"></div>
      <div class="contact-item">
        <svg viewBox="0 0 16 16" aria-hidden="true"><path d="M1 3h14v10H1V3zm1.4 1.2L8 8.6l5.6-4.4H2.4zM2.2 5.5v6.3h11.6V5.5L8 10 2.2 5.5z"/></svg>
        <span>DanaRWhitfield@clearbrookhp.com</span>
      </div>
    </div>
  </section>

  <section class="card card-brand" aria-label="Card back: company name">
    <div class="brand-lockup">
      <span class="brand-dot"></span>
      <span class="brand-name">Clearbrook Health Plans</span>
    </div>
    <div class="decor-square"></div>
  </section>

</main>
</body>
</html>
```